Business Cards for Harbourline Coatings Pty Ltd

Hi every one i need a design for my buisness cards. I Want my logo in it and the name of the company needs to stand out Harbourline Coatings Pty Ltd. I want the background of the buisness cards black and i want the font to stand out in either a white or a silver stylish text. I want the design to be simple but original not to in your face if you know what i mean. I want on the back of the buisness cards to have the services that my buisness offers.
• Interior/Exterior
• Residential/Commercial
• Special effects/Texture Coatings
• Water Damage Repair
• Fully qualified
• Pensioner Discount
• 10 Year guarantee
• Fully Insured
• Obligation free quotes
full internal repaints include a proffesionla cleaning service
I want the services on the back to be layed out in an originall way not just dot points. If possible could my logo take up the whole back ground of the back but the text with the services be kind of like transparent so u cvan still see the logo i dont know if its possible it woiuld just look cool if possible. When i pick a design ill give my contact details to the designer to add to the design at the end. Any questions please just ask! Ill upload my logo.
Conatcs will include office phone: Mobile: E-mail - dale@harbourlinecoatings.com.au, Ill also have a Postal address which is a PO Box and my website is www.harbourlinecoatings.com.au

```html
<!DOCTYPE html>
<html lang="en">
<head>
<meta charset="utf-8">
<title>Harbourline Coatings Pty Ltd – Business Cards</title>
<link rel="stylesheet" href="https://fonts.googleapis.com/css2?family=Montserrat:wght@600;700&family=Questrial&display=swap">
<style>
  :root {
    --page: #d6d6d6;
    --card: #050505;
    --card-soft: #161616;
    --green: #8dc63f;
    --white: #ffffff;
    --silver: #cfcfcf;
  }
  * { margin: 0; padding: 0; box-sizing: border-box; }
  html, body { width: 1200px; height: 765px; overflow: hidden; }
  body {
    background: var(--page);
    position: relative;
    font-family: "Montserrat", Arial, sans-serif;
  }
  .card {
    position: absolute;
    top: 302px;
    width: 573px;
    height: 343px;
    border-radius: 32px;
    background: var(--card);
    overflow: hidden;
  }
  .card--front { left: 17px; }
  .card--back { left: 605px; }
  .card__bands { position: absolute; inset: 0; width: 100%; height: 100%; }

  /* Front */
  .brand-mark {
    position: absolute;
    left: 96px; top: 36px;
    width: 136px; height: 136px;
    background: var(--green);
    border-radius: 10px;
  }
  .brand-front {
    position: absolute;
    left: 40px; top: 222px;
    transform: rotate(-13deg);
    transform-origin: left bottom;
    white-space: nowrap;
  }
  .brand-front__name {
    font-weight: 700;
    font-size: 31px;
    line-height: 36px;
    color: var(--white);
    letter-spacing: 0.5px;
    text-transform: uppercase;
  }
  .brand-front__suffix {
    font-weight: 700;
    font-size: 24px;
    line-height: 30px;
    color: var(--green);
    margin-left: 112px;
    text-transform: uppercase;
  }

  /* Back */
  .back-panel {
    position: absolute;
    left: 0; top: 0;
    width: 205px; height: 100%;
    background: var(--card-soft);
  }
  .back-circle {
    position: absolute;
    left: -70px; top: 110px;
    width: 230px; height: 230px;
    border-radius: 50%;
    border: 34px solid rgba(255,255,255,0.05);
  }
  .services {
    position: absolute;
    left: 46px; top: 80px;
    transform: rotate(-13deg);
    transform-origin: left bottom;
    white-space: nowrap;
    color: var(--green);
    font-size: 8.6px;
    font-weight: 600;
    line-height: 11px;
    letter-spacing: 0.6px;
    text-transform: uppercase;
  }
  .services__note { font-weight: 700; margin-top: 4px; }
  .brand-back {
    position: absolute;
    left: 45px; top: 146px;
    width: 124px;
    transform: rotate(-13deg);
    transform-origin: center center;
    text-align: center;
    white-space: nowrap;
  }
  .brand-back__mark {
    display: block;
    width: 32px; height: 32px;
    margin: 0 auto 4px;
    background: var(--green);
    border-radius: 3px;
  }
  .brand-back__name { font-size: 9.5px; line-height: 12px; font-weight: 700; color: var(--white); text-transform: uppercase; }
  .brand-back__suffix { font-size: 8px; line-height: 10px; font-weight: 700; color: var(--green); }
  .contact {
    position: absolute;
    left: 188px; top: 168px;
    transform: rotate(-13deg);
    transform-origin: left top;
    white-space: nowrap;
    color: var(--white);
  }
  .contact__name {
    font-family: "Questrial", Arial, sans-serif;
    font-size: 42px;
    letter-spacing: 6px;
    text-transform: uppercase;
    line-height: 48px;
    margin-bottom: 6px;
  }
  .contact__line {
    font-size: 11px;
    letter-spacing: 1.4px;
    line-height: 14px;
    text-transform: uppercase;
    color: var(--silver);
  }
  .contact__line b { color: var(--white); font-weight: 700; }
  .contact__line--post { font-size: 10px; color: var(--white); }
</style>
</head>
<body>

<section class="card card--front" aria-label="Business card front">
  <svg class="card__bands" viewBox="0 0 573 343" aria-hidden="true">
    <polygon points="0,175 573,30 573,110 0,255" fill="#ffffff" opacity="0.06"/>
    <line x1="0" y1="185" x2="573" y2="42" stroke="#e8e8e8" stroke-width="2" opacity="0.85"/>
    <line x1="0" y1="215" x2="573" y2="72" stroke="#bdbdbd" stroke-width="1.5" opacity="0.8"/>
    <line x1="240" y1="140" x2="573" y2="58" stroke="#ffffff" stroke-width="6" opacity="0.25"/>
  </svg>
  <div class="brand-mark"></div>
  <div class="brand-front">
    <div class="brand-front__name">Harbourline Coatings</div>
    <div class="brand-front__suffix">Pty Ltd</div>
  </div>
</section>

<section class="card card--back" aria-label="Business card back">
  <div class="back-panel"></div>
  <div class="back-circle"></div>
  <svg class="card__bands" viewBox="0 0 573 343" aria-hidden="true">
    <line x1="150" y1="155" x2="573" y2="45" stroke="#e0e0e0" stroke-width="2" opacity="0.85"/>
    <line x1="170" y1="175" x2="573" y2="72" stroke="#9a9a9a" stroke-width="1.5" opacity="0.7"/>
    <line x1="200" y1="320" x2="573" y2="222" stroke="#e0e0e0" stroke-width="2" opacity="0.85"/>
    <line x1="215" y1="340" x2="573" y2="248" stroke="#9a9a9a" stroke-width="1.5" opacity="0.7"/>
  </svg>

  <div class="services">
    <div>Interior/Exterior ::: Residential/Commercial</div>
    <div>Special Effects/Texture Coatings ::: Water Damage Repair</div>
    <div>Fully Qualified ::: Pensioner Discount ::: 10 Year Guarantee</div>
    <div>Fully Insured ::: Obligation Free Quotes</div>
    <div class="services__note">Full internal repaints include a professional cleaning service</div>
  </div>

  <div class="brand-back">
    <span class="brand-back__mark"></span>
    <div class="brand-back__name">Harbourline Coatings</div>
    <div class="brand-back__suffix">PTY LTD</div>
  </div>

  <div class="contact">
    <div class="contact__name">Sam Carter</div>
    <div class="contact__line">Tel : <b>0123456789</b></div>
    <div class="contact__line">Mob : <b>0123456789</b></div>
    <div class="contact__line">Email : <b>dale@harbourlinecoatings.com.au</b></div>
    <div class="contact__line">Website : <b>www.harbourlinecoatings.com.au</b></div>
    <div class="contact__line contact__line--post">PO Box Address 12345 Loremipsum Dolor</div>
  </div>
</section>

</body>
</html>
```